Torvel, Inc. new buisness cards - brand guide included

We need new business cards. SLEAK SIMPLE FINANCE. They must include a place for NAME, TITLE, CELL, OFFICE PHONE, EMAIL. they also must include our services across the bottom. AIR, OCEAN, FTL, LTL, EXPRESS. for reference this will be being handed to some of the most prestigious shipping companies in a america.

Target Market(s)

Finance and corporate

Contact Information for Business Card

We need new business cards. SLEAK SIMPLE FINANCE. They must include a place for NAME, TITLE, CELL, OFFICE PHONE, EMAIL. they also must include our services across the bottom. AIR, OCEAN, FTL, LTL, EXPRESS.

Requirements
Must have
• We need new business cards. SLEAK SIMPLE FINANCE. They must include a place for NAME, TITLE, CELL, OFFICE PHONE, EMAIL. they also must include our services across the bottom. AIR, OCEAN, FTL, LTL, EXPRESS.
Nice to have
• USE THE COLORS AND LOGO IN THE BRAND GUIDE :)

```html
<!DOCTYPE html>
<html lang="en">
<head>
<meta charset="utf-8">
<title>Torvel, Inc. — Business Card</title>
<link href="https://fonts.googleapis.com/css2?family=Libre+Baskerville:wght@400;700&family=Lora:wght@400&display=swap" rel="stylesheet">
<style>
  :root {
    --sand: #c4b495;
    --paper: #ffffff;
    --backdrop: #161616;
  }
  * { margin: 0; padding: 0; box-sizing: border-box; }
  html, body { width: 1189px; height: 1200px; overflow: hidden; background: var(--backdrop); }
  .canvas { position: relative; width: 1189px; height: 1200px; }
  .card {
    position: absolute; left: 169px; width: 851px; height: 485px;
    border-radius: 37px; overflow: hidden;
  }
  .card--front { top: 112px; background: var(--sand); }
  .card--back { top: 641px; background: var(--paper); }

  .wordmark {
    font-family: "Libre Baskerville", Georgia, serif;
    font-weight: 400; letter-spacing: 4px; line-height: 1;
    position: absolute; white-space: nowrap;
  }
  .card--front .wordmark {
    color: var(--paper); font-size: 72px;
    left: 50%; top: 50%; transform: translate(-50%, -50%);
  }
  .card--back .wordmark {
    color: var(--sand); font-size: 50px;
    left: 228px; top: 243px; transform: translate(-50%, -50%);
  }

  .divider {
    position: absolute; left: 425px; top: 165px;
    width: 2px; height: 155px; background: var(--sand);
  }
  .contact {
    position: absolute; left: 470px; top: 165px; color: var(--sand);
  }
  .contact__name {
    font-family: "Libre Baskerville", Georgia, serif; font-weight: 700;
    font-size: 25px; line-height: 1; margin-top: 0;
  }
  .contact__title {
    font-family: "Lora", Georgia, serif; font-size: 21px; line-height: 1;
    margin-top: 6px;
  }
  .contact__list { list-style: none; margin-top: 22px; }
  .contact__item {
    font-family: "Lora", Georgia, serif; font-size: 21px; line-height: 27px;
    display: flex; align-items: center; gap: 9px;
  }
  .contact__icon { width: 17px; height: 17px; flex: none; }

  .services {
    position: absolute; left: 0; right: 0; top: 388px; text-align: center;
    font-family: "Libre Baskerville", Georgia, serif; font-weight: 700;
    font-size: 23px; letter-spacing: 3px; color: var(--sand);
  }
  .services__sep { font-weight: 400; margin: 0 6px; }
  .band { position: absolute; left: 0; top: 0; width: 851px; height: 485px; }
</style>
</head>
<body>
<div class="canvas">
  <section class="card card--front">
    <div class="wordmark">TORVEL</div>
  </section>

  <section class="card card--back">
    <svg class="band" viewBox="0 0 851 485" aria-hidden="true">
      <path d="M0 395 Q425.5 545 851 395 L851 485 L0 485 Z" fill="var(--sand)"/>
    </svg>
    <div class="wordmark">TORVEL</div>
    <div class="divider"></div>
    <div class="contact">
      <p class="contact__name">ELENA R. MARSH</p>
      <p class="contact__title">Founder &amp; Director</p>
      <ul class="contact__list">
        <li class="contact__item">
          <svg class="contact__icon" viewBox="0 0 16 16" aria-hidden="true"><rect x="4" y="1.5" width="8" height="13" rx="1.2" fill="none" stroke="var(--sand)" stroke-width="1.6"/><rect x="7" y="12" width="2" height="1" fill="var(--sand)"/></svg>
          +1 55-210-7781
        </li>
        <li class="contact__item">
          <svg class="contact__icon" viewBox="0 0 16 16" aria-hidden="true"><path d="M1 6 Q8 0 15 6 L13 8 L11 6.5 L11 5 Q8 4 5 5 L5 6.5 L3 8 Z" fill="var(--sand)"/><path d="M4 9 L12 9 L13 14 L3 14 Z" fill="var(--sand)"/><circle cx="8" cy="11.5" r="1.4" fill="var(--paper)"/></svg>
          +1 55-210-7781
        </li>
        <li class="contact__item">
          <svg class="contact__icon" viewBox="0 0 16 16" aria-hidden="true"><rect x="1" y="3.5" width="14" height="9" fill="var(--sand)"/><path d="M1 3.5 L8 9 L15 3.5" fill="none" stroke="var(--paper)" stroke-width="1.2"/></svg>
          info@torvelmail.com
        </li>
      </ul>
    </div>
    <p class="services">AIR<span class="services__sep">|</span>OCEAN<span class="services__sep">|</span>FTL<span class="services__sep">|</span>LTL<span class="services__sep">|</span>EXPRESS</p>
  </section>
</div>
</body>
</html>
```